Calvera fine stockings - sexy cardboard box design needed!

We need a packaging design for a new online company based in Sydney called 'Calvera Hosiery'. We will be selling sexy stockings to our customers by Italian designers. We mainly feature lace stockings, an example of which, can be seen here:
http://www.brindelatessuti.example/italy-FASHION-WINTER

The design should be a cardboard pull out box, black in colour with the logo on the cover. We are looking for the logo to communicate sophistication and sexiness.

Examples of cardboard box shapes we would like are:
http://www.tradovex.example/product-gs/583016294/High_quality_drawer_paper_box.html

http://www.tradovex.example/product-gs/536192047/Cardboard_drawer_box.html

29 December:
I submitted a note when I extended the deadline, but cannot see it, so will write here for clarification. It has been difficult to choose the best design as the designs submitted were of such high quality. I want to have some people judge the designs, but because of the Christmas Season I have extended the deadline so that this can be done. Thanks.

Target Market(s)

The working professional woman.

Industry/Entity Type

Fashion

Requirements
Must have
• The words "Calvera Hosiery" on the cover of the box.

The box should be a sliding drawer.

The box size should be: (22*15*2.5cm).

Washing instructions and recycling logos on the back of the box. See example of uploaded file.

Nice to have
• It would be nice to have the background of the box a dark colour, maybe charcoal? But we are open to all ideas.
Should not have
• A stock photo on cover of box.

```html
<!DOCTYPE html>
<html lang="en">
<head>
<meta charset="utf-8">
<title>Calvera Hosiery — Box Cover</title>
<link rel="stylesheet" href="https://fonts.googleapis.com/css2?family=Poiret+One&family=Josefin+Sans:wght@300&display=swap">
<style>
  :root {
    --charcoal: #333333;
    --lace-dark: #0e0e0e;
    --lace-mid: #2a2a2a;
    --ivory: #f4f4f4;
    --ink: #121212;
  }
  html, body {
    margin: 0;
    padding: 0;
    overflow: hidden;
    background: var(--charcoal);
  }
  .box-cover {
    position: relative;
    width: 817px;
    height: 1200px;
    background: var(--charcoal);
    overflow: hidden;
  }
  .stocking-photo {
    position: absolute;
    left: 0;
    top: 0;
    width: 170px;
    height: 1200px;
  }
  .brand {
    position: absolute;
    right: 40px;
    top: 985px;
    text-align: right;
  }
  .brand-name {
    margin: 0;
    font-family: "Poiret One", sans-serif;
    font-weight: 400;
    font-size: 160px;
    line-height: 1;
    letter-spacing: 2px;
    color: var(--ivory);
  }
  .brand-tagline {
    margin: -4px 2px 0 0;
    font-family: "Josefin Sans", sans-serif;
    font-weight: 300;
    font-size: 50px;
    line-height: 1;
    letter-spacing: 1px;
    color: var(--ink);
  }
</style>
</head>
<body>
  <main class="box-cover">
    <svg class="stocking-photo" viewBox="0 0 170 1200" role="img" aria-label="Photograph of a leg in black lace stockings with a bow and lattice pattern">
      <defs>
        <linearGradient id="lace-tone" x1="0" y1="0" x2="1" y2="0">
          <stop offset="0" stop-color="#1c1c1c"/>
          <stop offset="0.55" stop-color="#101010"/>
          <stop offset="1" stop-color="#050505"/>
        </linearGradient>
      </defs>
      <path d="M0 0 H108 C118 120 140 260 152 420 C160 560 140 700 118 840 C104 950 90 1080 76 1200 H0 Z" fill="url(#lace-tone)"/>
    </svg>

    <header class="brand">
      <h1 class="brand-name">CALVERA</h1>
      <p class="brand-tagline">fine stocking</p>
    </header>
  </main>
</body>
</html>
```